Tampa Bay fishing guide needs stunning website.

I currently have a site - www.reelcoastcharters.example which I personally put together using the Plimo platform and I am looking for a redesign on a different platform (Sitebarn?) that will allow me to easily create landing pages in the future. Would like to have a block for visitors to opt in to newsletter. Need social media links on all pages.

I would like to let my visitors know that I am able to handle their fishing charter needs here in the Tampa Bay area, if I'm not available for the dates they are looking to go I can refer them to a reputable captain in the area.

Target Market(s)

United States

Industry/Entity Type

Tourism

Coding

Coded - Design and coding required

Number of Pages Required

5+ page

Font styles to use
Sans Serif

Colors
0355a3
3176b5
85abd2
fbf289

Requirements
Must have
• Mobile Responsive, Ability to insert Trackwise Metrics, Chatterly pixels, ability to add custom landing pages in future
Nice to have
• Clean, easy navigation

```html
<!DOCTYPE html>
<html lang="en">
<head>
<meta charset="utf-8">
<title>Capt. Reid Calloway – Tampa Bay Fishing Charters</title>
<link rel="stylesheet" href="https://fonts.googleapis.com/css2?family=Raleway:wght@400;500;600&family=Open+Sans:wght@400;600&display=swap">
<style>
:root{
  --blue:#1b6ad9;
  --blue-deep:#1c5fc6;
  --blue-light:#4c8ff0;
  --ink:#555;
  --ink-dark:#333;
  --grey-band:#efefef;
  --white:#fff;
  --line:#c9c9c9;
}
*{box-sizing:border-box;margin:0;padding:0}
html,body{width:1200px;height:2853px;overflow:hidden}
body{position:relative;font-family:"Open Sans",Arial,sans-serif;color:var(--ink);background:var(--white)}
.abs{position:absolute}

/* Header + hero */
.hero{left:0;top:0;width:1200px;height:708px;background:linear-gradient(160deg,#3d4a3a 0%,#5b6a52 35%,#6e7a6d 55%,#3b3f3a 80%,#2a2c2a 100%)}
.topbar{left:0;top:0;width:1200px;height:104px;background:linear-gradient(180deg,rgba(0,0,0,.55),rgba(0,0,0,.15))}
.brand{left:76px;top:30px;display:flex;align-items:center;gap:12px;font-family:"Raleway",sans-serif;font-weight:600;font-size:30px;color:var(--blue-light)}
.brand-dot{width:20px;height:20px;border-radius:50%;background:var(--blue-light)}
.call{left:866px;top:12px;height:26px;display:flex;align-items:center;font-size:15px;color:var(--white)}
.call .ico{width:36px;height:36px;border-radius:50%;background:var(--white);margin:0 12px 0 10px;display:flex;align-items:center;justify-content:center}
.nav{left:396px;top:57px;display:flex;align-items:center;font-family:"Open Sans",sans-serif;font-size:16px;color:#6fa4f2}
.nav a{color:inherit;text-decoration:none;white-space:nowrap}
.nav .active{color:var(--white);border:1px solid var(--white);padding:9px 20px}
.hero-caption{left:63px;top:483px;width:610px;height:198px;border:1px solid rgba(255,255,255,.6);background:rgba(0,0,0,.45);padding:14px 16px;font-family:"Raleway",sans-serif;font-size:35px;line-height:42px;color:var(--white)}

/* About */
.section-title{font-family:"Raleway",sans-serif;font-weight:400;text-transform:uppercase;color:var(--blue)}
.section-title span{color:#5b97f0}
.about-title{left:0;top:762px;width:1200px;text-align:center;font-size:48px}
.about-text{left:140px;top:852px;width:920px;text-align:center;font-size:16.5px;line-height:27px;color:#666}
.about-text p{margin-bottom:27px}

/* Newsletter */
.newsletter{left:0;top:1162px;width:1200px;height:154px;background:var(--blue)}
.nl-title{left:82px;top:1200px;font-family:"Raleway",sans-serif;font-size:58px;color:var(--white);letter-spacing:1px}
.nl-divider{left:491px;top:1186px;width:1px;height:106px;background:rgba(255,255,255,.45)}
.nl-tag{left:517px;top:1194px;font-family:"Raleway",sans-serif;font-size:23px;color:var(--white)}
.nl-input{left:517px;top:1238px;width:406px;height:46px;border:1px solid rgba(255,255,255,.8);padding:0 13px;line-height:44px;font-size:15px;color:var(--white)}
.nl-button{left:936px;top:1238px;width:186px;height:46px;background:var(--white);color:var(--blue);font-size:20px;text-align:center;line-height:46px;font-family:"Open Sans",sans-serif}

/* Gallery */
.shot{top:1390px;height:156px}
.shot-cap{top:1572px;width:256px;text-align:center;font-size:22px;color:#555;font-family:"Open Sans",sans-serif}
.shot-cap.first{color:var(--blue)}
.shot-desc{top:1640px;width:256px;text-align:center;font-size:14.5px;line-height:23px;color:#777}

/* Pick up + contact form */
.grey{left:0;top:1760px;width:1200px;height:519px;background:var(--grey-band)}
.pick-title{left:82px;top:1818px;font-size:46px}
.marina{left:76px;top:1890px;width:480px;text-align:center;font-size:28px;color:#555;font-family:"Raleway",sans-serif}
.address{left:76px;top:1934px;width:480px;text-align:center;font-size:17px;line-height:24px;color:#777}
.map{left:76px;top:1991px;width:479px;height:215px;background:linear-gradient(135deg,#e8e4da 0%,#dedad0 40%,#cfe3c6 60%,#a9cbe6 100%)}
.dots{left:280px;top:2232px;display:flex;gap:6px}
.dots i{display:block;width:16px;height:16px;border-radius:50%;border:2px solid var(--blue)}
.dots i.on{background:var(--blue)}
.split{left:599px;top:1826px;width:1px;height:380px;background:var(--line)}
.touch-title{left:645px;top:1818px;font-size:46px;color:var(--blue)}
.field{left:645px;width:416px;height:46px;background:#f2f2f2;border:1px solid #cfcfcf;padding:0 12px;line-height:44px;font-size:15px;color:#888}
.submit{left:645px;top:2161px;width:156px;height:42px;background:var(--blue);color:var(--white);font-size:20px;text-align:center;line-height:42px}

/* Contact band */
.contact-band{left:0;top:2279px;width:1200px;height:521px;background:linear-gradient(180deg,#5fa6e3 0%,#4f98dc 45%,#3f86d2 100%)}
.contact-panel{left:318px;top:2374px;width:565px;height:337px;background:rgba(120,170,240,.55)}
.contact-title{left:318px;top:2390px;width:565px;text-align:center;font-family:"Raleway",sans-serif;font-size:46px;color:var(--white)}
.c-row{display:flex;align-items:center;gap:16px;font-size:14.5px;color:var(--white)}
.c-ico{width:38px;height:38px;border-radius:50%;background:var(--white);display:flex;align-items:center;justify-content:center;flex:none}
.follow{left:318px;top:2578px;width:565px;text-align:center;font-size:13px;color:var(--white)}
.socials{left:528px;top:2617px;display:flex;gap:16px}
.socials span{display:block;width:42px;height:42px;border-radius:50%;background:var(--white)}
.socials span+span{background:transparent;border:2px solid var(--white)}

/* Footer */
.footer{left:0;top:2800px;width:1200px;height:53px;background:var(--blue-deep);text-align:center;line-height:53px;font-size:13.5px;color:#dfe9fb}
</style>
</head>
<body>

<!-- Hero -->
<div class="abs hero" role="img" aria-label="Photo of a smiling angler in waders holding up a freshly caught trout beside a river"></div>
<div class="abs topbar"></div>
<div class="abs brand"><span class="brand-dot"></span>Capt. Reid Calloway</div>
<div class="abs call">Call Capt. Reid
  <span class="ico"><svg width="18" height="18" viewBox="0 0 24 24"><path d="M6.6 10.8a15 15 0 0 0 6.6 6.6l2.2-2.2c.3-.3.7-.4 1-.2 1.1.4 2.3.6 3.6.6.6 0 1 .4 1 1V20c0 .6-.4 1-1 1A17 17 0 0 1 3 4c0-.6.4-1 1-1h3.5c.6 0 1 .4 1 1 0 1.3.2 2.5.6 3.6.1.3 0 .7-.2 1z" fill="#1b6ad9"/></svg></span>(555) 014-2290</div>
<nav class="abs nav">
  <a class="active" href="#">HOME</a>
  <a href="#" style="margin-left:21px">ABOUT US</a>
  <a href="#" style="margin-left:36px">PICK UP LOCATION</a>
  <a href="#" style="margin-left:28px">RATES</a>
  <a href="#" style="margin-left:32px">CONTACT US</a>
  <a href="#" style="margin-left:30px">GIFT CARD</a>
</nav>
<div class="abs hero-caption">Come fish with Tampa Bay, FL fishing guide, Tampa Bay fishing charter most respected Captain, 25 year Native Guide.</div>

<!-- About -->
<h2 class="abs section-title about-title">About <span>Us</span></h2>
<div class="abs about-text">
  <p>Capt. Reid Calloway, with over 20 years' experience, Native fishing charter tampa charter captain offering full and half day fishing charters on the waters of Tampa Bay.</p>
  <p>If you're looking for a great fishing charter tampa don't hesitate to contact Capt. Reid or you can simply book your trip online here.</p>
  <p>Come enjoy a wonderful day fishing charters Tampa for Tarpon, Snook, Redfish, Trout, Sharks, Cobia, Spanish mackerel as well as others aboard Capt. Reid Calloway Sport fishing Charters boat. Capt. Reid will work hard to ensure that you and your guests have a memorable day enjoying the wonderful gamefish that Tampa Bay has to offer.</p>
</div>

<!-- Newsletter -->
<div class="abs newsletter"></div>
<div class="abs nl-title">NEWSLETTER</div>
<div class="abs nl-divider"></div>
<div class="abs nl-tag">everything fishing and boating</div>
<div class="abs nl-input">Enter Email Id</div>
<div class="abs nl-button">SUBSCRIBE</div>

<!-- Gallery -->
<div class="abs shot" style="left:76px;width:257px;background:linear-gradient(180deg,#8fb4d8,#c9c2a8);border:2px solid #333" role="img" aria-label="Photo of two anglers with rods filming a fishing show"></div>
<div class="abs shot" style="left:340px;width:255px;background:linear-gradient(180deg,#6f8e6a,#4b74a8)" role="img" aria-label="Photo of the captain holding a large fish on the water"></div>
<div class="abs shot" style="left:605px;width:253px;background:linear-gradient(180deg,#dcdcd6,#9ea7a0)" role="img" aria-label="Photo of two men fishing for tarpon from a boat"></div>
<div class="abs shot" style="left:869px;width:253px;background:linear-gradient(160deg,#2f7f6c,#d7d7d2)" role="img" aria-label="Photo of anglers landing a fish beside the boat"></div>

<div class="abs shot-cap first" style="left:76px">Capt. Reid and Mark<br>Dorran</div>
<div class="abs shot-cap" style="left:340px">Capt. Reid</div>
<div class="abs shot-cap" style="left:604px">Capt. Reid with Wade<br>Hollis</div>
<div class="abs shot-cap" style="left:868px">Capt. Reid and Roland<br>Pike</div>
<div class="abs shot-desc" style="left:76px;top:1644px">Filming a show for Mark Dorran's<br>Coastal Journal</div>
<div class="abs shot-desc" style="left:340px;top:1644px">Capt. Reid with one of his Tarpon<br>friends</div>
<div class="abs shot-desc" style="left:604px;top:1644px">Hall of Famer Wade Hollis and Capt.<br>Reid Tarpon fishing on Tampa Bay</div>
<div class="abs shot-desc" style="left:868px;top:1644px">Roland Pike with Capt. Reid<br>heading out for some fun on Tampa<br>Bay</div>

<!-- Pick up + form -->
<div class="abs grey"></div>
<h2 class="abs section-title pick-title">Pick Up <span>Location</span></h2>
<div class="abs marina">HARBOR POINT MARINA</div>
<div class="abs address">4820 Bayview Street South<br>St. Petersburg, FL 33700</div>
<div class="abs map" role="img" aria-label="Street map showing the marina pick up location"></div>
<div class="abs dots"><i class="on"></i><i></i><i></i><i></i></div>
<div class="abs split"></div>
<h2 class="abs touch-title" style="font-family:'Raleway',sans-serif;font-weight:400">GET In TOUCH</h2>
<div class="abs field" style="top:1900px">Enter Name</div>
<div class="abs field" style="top:1950px">Enter Contact No.</div>
<div class="abs field" style="top:2001px">Enter E Mail Id</div>
<div class="abs field" style="top:2052px;height:97px">Enter Message...</div>
<div class="abs submit">SUBMIT</div>

<!-- Contact -->
<div class="abs contact-band" role="img" aria-label="Underwater photo of tarpon swimming in blue water"></div>
<div class="abs contact-panel"></div>
<div class="abs contact-title">CONTACT US</div>
<div class="abs c-row" style="left:424px;top:2463px">
  <span class="c-ico"><svg width="18" height="18" viewBox="0 0 24 24"><path d="M6.6 10.8a15 15 0 0 0 6.6 6.6l2.2-2.2c.3-.3.7-.4 1-.2 1.1.4 2.3.6 3.6.6.6 0 1 .4 1 1V20c0 .6-.4 1-1 1A17 17 0 0 1 3 4c0-.6.4-1 1-1h3.5c.6 0 1 .4 1 1 0 1.3.2 2.5.6 3.6.1.3 0 .7-.2 1z" fill="none" stroke="#4f98dc" stroke-width="1.6"/></svg></span>555-014-2290
</div>
<div class="abs c-row" style="left:592px;top:2463px">
  <span class="c-ico"><svg width="20" height="16" viewBox="0 0 20 16"><rect x="1" y="1" width="18" height="14" rx="2" fill="none" stroke="#4f98dc" stroke-width="1.6"/><path d="M1.5 2l8.5 7 8.5-7" fill="none" stroke="#4f98dc" stroke-width="1.6"/></svg></span>captreid@mailbox.example
</div>
<div class="abs c-row" style="left:424px;top:2514px">
  <span class="c-ico"><svg width="16" height="20" viewBox="0 0 16 20"><path d="M8 19s-6-6.5-6-11a6 6 0 0 1 12 0c0 4.5-6 11-6 11z" fill="none" stroke="#4f98dc" stroke-width="1.6"/><circle cx="8" cy="8" r="2.2" fill="none" stroke="#4f98dc" stroke-width="1.6"/></svg></span>123,Lorem Ipsum,City,Country,Zip code
</div>
<div class="abs follow">FOLLOW US ON</div>
<div class="abs socials">
  <span role="img" aria-label="Chatterly"></span>
  <span role="img" aria-label="Chirpline"></span>
  <span role="img" aria-label="Circlecast"></span>
</div>

<!-- Footer -->
<div class="abs footer">© Capt. Reid Calloway - 2016 All Right Reserved</div>

</body>
</html>
```